Pain Seminar Flyer 8.5x11

We are having a FREE seminar on Pain for our Bootcamp members at our gym. We are looking for a great looking flyer with pictures and a design to draw people in. I have attached our logo, pictures of the 2 speakers and a Word document of the flyer information needed. PLEASE PLEASE make our head shots small and in a circle like the example flyer we attached but obviously make the flyer much much nicer than the example. Also we attached pic ideas about pain.
- This must be in PSD. format WITH LAYERS and fonts so we can edit the time or reuse the flyer.
- Size 8.5x11
- Attached info. with pics and logo (along with other pics of pain!)
Thank you!
Gym

```html
<!DOCTYPE html>
<html lang="en">
<head>
<meta charset="utf-8">
<title>Free Seminar on How to Stop Pain</title>
<link href="https://fonts.googleapis.com/css2?family=Lato:wght@300;400;700;900&display=swap" rel="stylesheet">
<style>
  :root{
    --blue:#1b74b9;
    --ink:#2b2b2d;
    --paper:#e9e9ea;
    --dark:#1d1d1f;
    --dark-2:#2c2c2e;
    --white:#ffffff;
    --muted:#d9d9da;
  }
  *{margin:0;padding:0;box-sizing:border-box}
  html,body{width:1200px;height:970px;overflow:hidden;background:var(--paper)}
  body{font-family:"Lato",Arial,sans-serif;color:var(--ink)}
  .flyer{position:relative;width:1200px;height:970px;background:var(--paper);overflow:hidden}

  .header{position:absolute;left:0;top:0;width:1200px;height:220px;text-align:center}
  .header__title{position:absolute;left:0;right:0;top:26px;font-weight:900;font-size:104px;letter-spacing:3px;color:var(--blue);line-height:1}
  .header__sub{position:absolute;left:0;right:0;top:138px;font-weight:300;font-size:74px;letter-spacing:2px;color:var(--ink);line-height:1}
  .header__sub strong{font-weight:900}

  .pain-strip{position:absolute;left:0;top:212px;width:1200px;height:344px;display:flex}
  .pain-strip__panel{flex:1;height:100%}
  .panel--hip{background:radial-gradient(circle at 60% 35%,#e0375a 0,#7a3fa8 22%,#3a3f9e 55%,#23286e 100%)}
  .panel--shoulder{background:radial-gradient(circle at 45% 30%,#f05a6a 0,#7c74c8 25%,#3f6cc2 55%,#1f3d88 100%)}
  .panel--knee{background:radial-gradient(circle at 50% 50%,#e8506a 0,#c42f55 30%,#6c3b9a 60%,#2a3590 100%)}
  .panel--wrist{background:radial-gradient(circle at 45% 60%,#ff8a3a 0,#e0452b 30%,#3a52b0 62%,#1e3a8c 100%)}
  .panel--ankle{background:radial-gradient(circle at 60% 45%,#ffb347 0,#f06a28 28%,#2f7ad0 62%,#1d4ca6 100%)}

  .tear{position:absolute;left:0;width:1200px;height:24px;display:block}
  .tear--top{top:200px}
  .tear--mid{top:544px}
  .tear--bottom{top:900px}

  .info{position:absolute;left:0;top:556px;width:1200px;height:350px;background:radial-gradient(ellipse at 40% 40%,var(--dark-2) 0,var(--dark) 70%)}

  .questions{position:absolute;left:44px;top:600px;font-weight:700;font-size:34px;letter-spacing:1px;line-height:42px;color:var(--white)}
  .questions .is-accent{color:var(--blue)}

  .topics{position:absolute;left:44px;top:732px;list-style:none;font-weight:400;font-size:21px;letter-spacing:.8px;color:var(--muted)}
  .topics li{display:flex;align-items:center;height:31px}
  .topics svg{width:18px;height:18px;margin-right:14px;flex:none}

  .booking{position:absolute;left:609px;top:566px;font-weight:700;font-size:25px;letter-spacing:.8px;line-height:35px;color:var(--white)}
  .booking .is-accent{color:var(--blue)}

  .date-bar{position:absolute;left:584px;top:680px;width:616px;height:42px;background:var(--blue);color:var(--white);font-weight:700;font-size:26px;letter-spacing:1px;line-height:42px;padding-left:62px;box-shadow:0 4px 6px rgba(0,0,0,.45)}
  .date-bar__fold{position:absolute;left:584px;top:668px;width:14px;height:12px;display:block}

  .speaker{position:absolute;top:738px;width:150px;text-align:center;color:var(--white);font-size:10px;font-weight:400}
  .speaker--one{left:585px}
  .speaker--two{left:732px}
  .speaker__photo{display:block;width:108px;height:108px;margin:0 auto 14px;border-radius:50%;border:4px solid var(--white);background:radial-gradient(circle at 50% 40%,#c9a690 0,#8a7766 45%,#4a4f46 100%);box-shadow:0 3px 6px rgba(0,0,0,.6)}

  .brand{position:absolute;left:932px;top:790px;width:248px;height:76px;display:flex;align-items:center;justify-content:center;gap:10px;font-weight:900;font-size:21px;letter-spacing:1px;color:var(--white)}
  .brand__mark{width:16px;height:16px;background:var(--blue)}

  .footer-url{position:absolute;left:44px;top:922px;font-weight:700;font-size:23px;letter-spacing:.6px;color:var(--dark)}
</style>
</head>
<body>
<main class="flyer">
  <header class="header">
    <h1 class="header__title">FREE SEMINAR</h1>
    <p class="header__sub">ON HOW TO <strong>STOP PAIN</strong></p>
  </header>

  <section class="pain-strip">
    <div class="pain-strip__panel panel--hip" role="img" aria-label="X-ray style illustration of a hip joint glowing red with pain"></div>
    <div class="pain-strip__panel panel--shoulder" role="img" aria-label="X-ray style illustration of a shoulder joint glowing red with pain"></div>
    <div class="pain-strip__panel panel--knee" role="img" aria-label="X-ray style illustration of a knee joint glowing red with pain"></div>
    <div class="pain-strip__panel panel--wrist" role="img" aria-label="X-ray style illustration of a wrist and hand glowing orange with pain"></div>
    <div class="pain-strip__panel panel--ankle" role="img" aria-label="X-ray style illustration of an ankle and foot glowing orange with pain"></div>
  </section>

  <svg class="tear tear--top" viewBox="0 0 1200 24" preserveAspectRatio="none" aria-hidden="true">
    <path fill="#ffffff" d="M0 0H1200V10L1170 16 1140 9 1100 15 1060 8 1020 14 980 10 940 17 900 9 860 14 820 8 780 15 740 10 700 16 660 8 620 13 580 9 540 16 500 10 460 15 420 8 380 14 340 9 300 16 260 10 220 15 180 8 140 14 100 9 60 16 30 10 0 14Z"/>
  </svg>
  <svg class="tear tear--mid" viewBox="0 0 1200 24" preserveAspectRatio="none" aria-hidden="true">
    <path fill="#ffffff" d="M0 6L30 2 70 8 110 3 150 9 190 4 230 10 270 3 310 8 350 2 390 9 430 4 470 10 510 3 550 8 590 2 630 9 670 4 710 10 750 3 790 8 830 2 870 9 910 4 950 10 990 3 1030 8 1070 2 1110 9 1150 4 1200 8V16L1160 20 1120 14 1080 21 1040 15 1000 20 960 14 920 21 880 15 840 20 800 14 760 21 720 15 680 20 640 14 600 21 560 15 520 20 480 14 440 21 400 15 360 20 320 14 280 21 240 15 200 20 160 14 120 21 80 15 40 20 0 15Z"/>
  </svg>

  <section class="info" aria-label="Seminar details"></section>

  <div class="questions">
    <p>BACK PAIN?</p>
    <p class="is-accent">SHOULDER PAIN?</p>
    <p>KNEE PAIN?</p>
  </div>

  <ul class="topics">
    <li><svg viewBox="0 0 18 18" aria-hidden="true"><circle cx="9" cy="9" r="7.5" fill="none" stroke="#1b74b9" stroke-width="1.6"/><path d="M5.5 9.2l2.3 2.3 4.6-4.8" fill="none" stroke="#1b74b9" stroke-width="1.8"/></svg>How to Get Out of Pain</li>
    <li><svg viewBox="0 0 18 18" aria-hidden="true"><circle cx="9" cy="9" r="7.5" fill="none" stroke="#1b74b9" stroke-width="1.6"/><path d="M5.5 9.2l2.3 2.3 4.6-4.8" fill="none" stroke="#1b74b9" stroke-width="1.8"/></svg>What to do When an Exercise Hurts</li>
    <li><svg viewBox="0 0 18 18" aria-hidden="true"><circle cx="9" cy="9" r="7.5" fill="none" stroke="#1b74b9" stroke-width="1.6"/><path d="M5.5 9.2l2.3 2.3 4.6-4.8" fill="none" stroke="#1b74b9" stroke-width="1.8"/></svg>How Exercise Helps Pain</li>
    <li><svg viewBox="0 0 18 18" aria-hidden="true"><circle cx="9" cy="9" r="7.5" fill="none" stroke="#1b74b9" stroke-width="1.6"/><path d="M5.5 9.2l2.3 2.3 4.6-4.8" fill="none" stroke="#1b74b9" stroke-width="1.8"/></svg>Q &amp; A to Fine Extraordinary Health</li>
  </ul>

  <div class="booking">
    <p>RESERVATIONS REQUIRED.</p>
    <p class="is-accent">CALL 555-010-4827 TODAY</p>
    <p>LIMITED SPACE SO DON’T WAIT TO SIGN UP</p>
  </div>

  <svg class="date-bar__fold" viewBox="0 0 14 12" aria-hidden="true"><path d="M14 0V12H0Z" fill="#0f4f80"/></svg>
  <div class="date-bar">THURSDAY, APRIL 13th 7:30PM-9PM</div>

  <figure class="speaker speaker--one">
    <span class="speaker__photo" role="img" aria-label="Circular headshot of speaker Owen Mercer"></span>
    <figcaption>Owen Mercer, PT, DPT, OCS</figcaption>
  </figure>
  <figure class="speaker speaker--two">
    <span class="speaker__photo" role="img" aria-label="Circular headshot of speaker Dale Harlan"></span>
    <figcaption>Dale Harlan, MS, CSCS, FMS</figcaption>
  </figure>

  <div class="brand"><span class="brand__mark" aria-hidden="true"></span>STRIDEWELL BOOTCAMPS</div>

  <svg class="tear tear--bottom" viewBox="0 0 1200 24" preserveAspectRatio="none" aria-hidden="true">
    <path fill="#e9e9ea" d="M0 8L40 3 80 10 120 4 160 9 200 2 240 8 280 4 320 11 360 3 400 9 440 4 480 10 520 2 560 8 600 4 640 11 680 3 720 9 760 4 800 10 840 2 880 8 920 4 960 11 1000 3 1040 9 1080 4 1120 10 1160 3 1200 8V24H0Z"/>
    <path fill="#ffffff" d="M0 8L40 3 80 10 120 4 160 9 200 2 240 8 280 4 320 11 360 3 400 9 440 4 480 10 520 2 560 8 600 4 640 11 680 3 720 9 760 4 800 10 840 2 880 8 920 4 960 11 1000 3 1040 9 1080 4 1120 10 1160 3 1200 8V14L1160 17 1120 13 1080 18 1040 14 1000 17 960 13 920 18 880 14 840 17 800 13 760 18 720 14 680 17 640 13 600 18 560 14 520 17 480 13 440 18 400 14 360 17 320 13 280 18 240 14 200 17 160 13 120 18 80 14 40 17 0 14Z"/>
  </svg>

  <p class="footer-url">www.Stridewell.com</p>
</main>
</body>
</html>
```